Business Card design for shipping company 'FARNHOLT MARITIME LTD'

Classic / traditional business card in black Garamond / Times New Roman or similar text for a shipping / marine transport company, containing the following information:

QUOTE

FARNHOLT MARITIME LTD

PETER CALLOWAY FICS

T: +44 7923 615087
E: vessels@farnholt-mar.com

UNQUOTE

Target Market(s)

Marine / Shipping industry

Contact Information for Business Card

FARNHOLT MARITIME LTD PETER CALLOWAY FICS T: +44 7923 615087 E: vessels@farnholt-mar.com

Font styles to use
Serif

Colors

Designer to choose colors to be used in the design.

Requirements
Must have
• Garamond / Times New Roman or similar text in black colour

```html
<!DOCTYPE html>
<html lang="en">
<head>
<meta charset="utf-8">
<title>Farnholt Maritime Ltd – Business Card</title>
<link href="https://fonts.googleapis.com/css2?family=Tinos:wght@400;700&display=swap" rel="stylesheet">
<style>
  :root {
    --backdrop: #1e1e1e;
    --paper: #ffffff;
    --ink: #111111;
    --accent: #e0321f;
    --card-dark: #1a1717;
    --serif: "Tinos", "Times New Roman", serif;
  }
  * { margin: 0; padding: 0; box-sizing: border-box; }
  html, body {
    width: 1200px;
    height: 900px;
    overflow: hidden;
    background: var(--backdrop);
    font-family: var(--serif);
  }
  .stage {
    position: relative;
    width: 1200px;
    height: 900px;
  }
  .card {
    position: absolute;
    width: 560px;
    height: 320px;
    border-radius: 28px;
    overflow: hidden;
  }
  .card--front {
    left: 70px;
    top: 100px;
    background: var(--paper);
  }
  .card--back {
    left: 570px;
    top: 480px;
    background: var(--card-dark);
  }
  .brand {
    position: absolute;
    display: flex;
    align-items: center;
    gap: 10px;
    color: var(--accent);
    font-weight: 700;
    font-size: 26px;
    letter-spacing: 1px;
    white-space: nowrap;
  }
  .brand__mark {
    width: 18px;
    height: 18px;
    background: var(--accent);
  }
  .card--front .brand {
    left: 110px;
    top: 62px;
  }
  .card--back .brand {
    left: 50%;
    top: 50%;
    transform: translate(-50%, -50%);
  }
  .holder {
    position: absolute;
    left: 0;
    right: 0;
    top: 168px;
    text-align: center;
    color: var(--accent);
    font-size: 22px;
    letter-spacing: 0.5px;
  }
  .contact {
    position: absolute;
    left: 0;
    right: 0;
    top: 210px;
    text-align: center;
    color: var(--ink);
    font-size: 17px;
  }
  .contact__label { color: var(--accent); }
  .front-rule {
    position: absolute;
    left: 0;
    right: 0;
    top: 286px;
    height: 2px;
    background: var(--accent);
  }
</style>
</head>
<body>
  <main class="stage">
    <section class="card card--front" aria-label="Business card front">
      <div class="brand"><span class="brand__mark"></span>FARNHOLT MARITIME LTD</div>
      <p class="holder">PETER CALLOWAY FICS</p>
      <p class="contact">
        <span class="contact__label">T:</span> +44 7923 615087
        <span class="contact__label">E:</span> vessels@farnholt-mar.com
      </p>
      <div class="front-rule"></div>
    </section>

    <section class="card card--back" aria-label="Business card back">
      <div class="brand"><span class="brand__mark"></span>FARNHOLT MARITIME LTD</div>
    </section>
  </main>
</body>
</html>
```